Morvela Aesthetic Doctor

I require an elegant, luxurious looking business card for my aesthetic business. I am a doctor and that will set me aside from competitors. I am planning to provide home and spa based treatments to clients with high expectations. I have attached my logo.

```html
<!DOCTYPE html>
<html lang="en">
<head>
<meta charset="utf-8">
<title>Morvela Aesthetic Doctor – Business Card</title>
<link href="https://fonts.googleapis.com/css2?family=Open+Sans:wght@300;400;600&display=swap" rel="stylesheet">
<style>
  :root {
    --page: #f1f2f4;
    --card: #ffffff;
    --brand-blue: #2a6ab3;
    --sky: #4fb0e4;
    --light-sky: #a6d8f0;
    --deep-blue: #1f74c4;
    --grey-text: #8a8d92;
    --ink: #3b3e44;
    --swoosh: #e3e5e8;
  }
  * { margin: 0; padding: 0; box-sizing: border-box; }
  html, body {
    width: 763px; height: 1200px; overflow: hidden;
    background: var(--page);
    font-family: "Open Sans", Arial, sans-serif;
  }
  .sheet { position: relative; width: 763px; height: 1200px; }
  .card {
    position: absolute; left: 62px; width: 640px; height: 356px;
    background: var(--card); overflow: hidden;
    box-shadow: 0 10px 28px rgba(0,0,0,0.14);
  }
  .card--front { top: 190px; }
  .card--back { top: 650px; }

  /* front */
  .portrait-art {
    position: absolute; left: 0; top: 0; width: 210px; height: 356px;
    background: linear-gradient(180deg, var(--sky) 0%, var(--deep-blue) 45%, var(--sky) 72%, var(--light-sky) 100%);
  }
  .brand { position: absolute; display: flex; align-items: center; }
  .brand__dot { border: 2px solid var(--sky); border-radius: 50%; flex: none; }
  .brand__name { color: var(--grey-text); font-weight: 300; letter-spacing: 0.04em; line-height: 1; }
  .brand__tag { color: var(--sky); font-weight: 400; letter-spacing: 0.1em; line-height: 1; margin-top: 4px; }
  .card--front .brand { left: 300px; top: 145px; }
  .card--front .brand__dot { width: 54px; height: 54px; margin-right: 14px; }
  .card--front .brand__name { font-size: 44px; }
  .card--front .brand__tag { font-size: 15px; }

  /* back */
  .swoosh-art {
    position: absolute; right: 0; top: 0; width: 380px; height: 230px;
    background: radial-gradient(ellipse at 90% 10%, var(--swoosh) 0%, #eef0f2 45%, rgba(255,255,255,0) 75%);
  }
  .card--back .brand { left: 40px; top: 50px; }
  .card--back .brand__dot { width: 34px; height: 34px; margin-right: 8px; }
  .card--back .brand__name { font-size: 26px; }
  .card--back .brand__tag { font-size: 9px; }

  .doctor { position: absolute; left: 40px; top: 150px; }
  .doctor__name { color: var(--brand-blue); font-size: 22px; font-weight: 600; }
  .doctor__rule { width: 40px; height: 1px; background: var(--ink); margin: 4px 0 3px; }
  .doctor__title { color: var(--ink); font-size: 11px; font-weight: 600; }
  .doctor__diploma { color: var(--ink); font-size: 7px; }

  .contact { position: absolute; left: 380px; top: 118px; list-style: none; }
  .contact__item { display: flex; align-items: center; color: var(--ink); font-size: 15px; line-height: 21px; }
  .contact__icon {
    width: 13px; height: 13px; border-radius: 50%; background: var(--sky);
    margin-right: 6px; display: flex; align-items: center; justify-content: center; flex: none;
  }
  .contact__icon svg { width: 9px; height: 9px; }

  .services {
    position: absolute; right: 40px; top: 250px; text-align: right;
    color: var(--ink); font-size: 11px; line-height: 16px;
  }
  .services__dot { color: var(--brand-blue); margin: 0 4px; }

  .band {
    position: absolute; left: 0; bottom: 0; width: 100%; height: 34px;
    background: var(--brand-blue); color: #fff; font-size: 11px;
    display: flex; align-items: center; justify-content: flex-end; padding-right: 150px;
  }
</style>
</head>
<body>
<main class="sheet">

  <section class="card card--front" aria-label="Card front">
    <div class="portrait-art" role="img" aria-label="Layered blue profile illustration"></div>
    <div class="brand">
      <span class="brand__dot"></span>
      <div>
        <div class="brand__name">MORVELA</div>
        <div class="brand__tag">AESTHETIC DOCTOR</div>
      </div>
    </div>
  </section>

  <section class="card card--back" aria-label="Card back">
    <div class="swoosh-art" role="img" aria-label="Soft grey flowing curves"></div>
    <div class="brand">
      <span class="brand__dot"></span>
      <div>
        <div class="brand__name">MORVELA</div>
        <div class="brand__tag">AESTHETIC DOCTOR</div>
      </div>
    </div>

    <div class="doctor">
      <div class="doctor__name">Dr Elina Varga</div>
      <div class="doctor__rule"></div>
      <div class="doctor__title">MRCPCH MD</div>
      <div class="doctor__diploma">Australasian Diploma of Aesthetic Medicine</div>
    </div>

    <ul class="contact">
      <li class="contact__item">
        <span class="contact__icon"><svg viewBox="0 0 10 10"><path d="M2 1l2 2-1 1c.6 1.3 1.7 2.4 3 3l1-1 2 2-1.2 1.2C4.5 9 1 5.5 .8 2.2z" fill="#fff"/></svg></span>
        0800 555 014
      </li>
      <li class="contact__item">
        <span class="contact__icon"><svg viewBox="0 0 10 10"><rect x="1" y="2.5" width="8" height="5" fill="none" stroke="#fff"/><path d="M1 2.5l4 3 4-3" fill="none" stroke="#fff"/></svg></span>
        elina@morvela.co.nz
      </li>
      <li class="contact__item">
        <span class="contact__icon"><svg viewBox="0 0 10 10"><circle cx="5" cy="5" r="3.6" fill="none" stroke="#fff" stroke-width=".8"/><ellipse cx="5" cy="5" rx="1.5" ry="3.6" fill="none" stroke="#fff" stroke-width=".8"/><path d="M1.4 5h7.2" stroke="#fff" stroke-width=".8"/></svg></span>
        www.morvela.co.nz
      </li>
    </ul>

    <div class="services">
      <div>Dermal injectables<span class="services__dot">●</span>Plasma facials<span class="services__dot">●</span>Microneedling</div>
      <div>Skin boosters<span class="services__dot">●</span>Excessive sweating</div>
    </div>

    <div class="band">Home and Spa Based Treatments</div>
  </section>

</main>
</body>
</html>
```